Inspirational Quotes Poster Set

Braxlune is a stylish coworking space, which has a design-oriented vintage look from the 60's with an industrial touch (www.braxlune-example.com) Braxlune Quote Poster Set of 16 posters. The poster should be typo oriented and rather simple. Reflecting a bit the clean billboard design from the sixties. Minimal / simple graphical elements

Target Market(s)

Startups and Entrepreneurs

Industry/Entity Type

Startup

Font styles to use
Sans Serif

Colors

Designer to choose colors to be used in the design.

Requirements
Must have
• Posters need to be on and very stylish

```html
<!DOCTYPE html>
<html lang="en">
<head>
<meta charset="utf-8">
<title>Braxlune Quote Poster – Never Give Up</title>
<link rel="stylesheet" href="https://fonts.googleapis.com/css2?family=Archivo:wdth,wght@125,600;125,700;125,800&display=swap">
<style>
  :root {
    --teal: #14a19a;
    --band: #06735f;
    --ink: #ffffff;
    --muted: #6f9690;
  }
  html, body {
    margin: 0;
    padding: 0;
    overflow: hidden;
  }
  body {
    width: 801px;
    height: 1200px;
    background: var(--teal);
  }
  .poster {
    position: relative;
    width: 801px;
    height: 1200px;
    overflow: hidden;
    background: var(--teal);
    font-family: "Archivo", "Helvetica Neue", Arial, sans-serif;
    font-stretch: 125%;
  }
  .headline {
    position: absolute;
    inset: 0;
    width: 801px;
    height: 1200px;
  }
  .headline text {
    font-family: "Archivo", "Helvetica Neue", Arial, sans-serif;
    font-stretch: 125%;
  }
  .never {
    font-weight: 600;
    font-size: 234px;
    fill: var(--ink);
  }
  .give-up {
    font-weight: 800;
    font-size: 90px;
    fill: var(--ink);
  }
  .give-up--shaded {
    fill: var(--muted);
  }
  .attribution {
    position: absolute;
    left: 70px;
    top: 1018px;
    margin: 0;
    color: var(--ink);
    font-weight: 700;
    font-size: 21px;
    line-height: 28px;
  }
  .brand-name {
    position: absolute;
    left: 70px;
    top: 1096px;
    margin: 0;
    color: var(--ink);
    font-weight: 800;
    font-size: 46px;
    line-height: 1;
    letter-spacing: -1px;
  }
</style>
</head>
<body>
  <main class="poster">
    <svg class="headline" viewBox="0 0 801 1200" aria-label="Never never never give up.">
      <defs>
        <clipPath id="band-clip">
          <rect x="438" y="833" width="363" height="21"/>
        </clipPath>
      </defs>
      <text class="never" x="-4" y="411" textLength="830" lengthAdjust="spacingAndGlyphs">NEVER</text>
      <text class="never" x="-4" y="600" textLength="830" lengthAdjust="spacingAndGlyphs">NEVER</text>
      <text class="never" x="-4" y="788" textLength="830" lengthAdjust="spacingAndGlyphs">NEVER</text>

      <rect class="band" x="438" y="833" width="363" height="21" fill="var(--band)"/>
      <text class="give-up" x="456" y="867" textLength="327" lengthAdjust="spacingAndGlyphs">give up.</text>
      <text class="give-up give-up--shaded" x="456" y="867" textLength="327" lengthAdjust="spacingAndGlyphs" clip-path="url(#band-clip)">give up.</text>
    </svg>

    <p class="attribution">Walter Crandell,<br>British Prime Minister</p>
    <p class="brand-name">Braxlune</p>
  </main>
</body>
</html>
```